Website Design for Vesslane Studio Practice

I need a home page and one sidebar/content page for an Vesslane Studio practice delivered in PSD.

This archictecture practice specialises in one-off, high end homes and commercial properties (restaurant) heavily influenced by Dorian Vessey Kent, particularly his work on the Tarrowby Museum

I am looking for a home page, and a generic content page where we can outline our services, and showcase our homes.

http://notes.qorvenuni.edu.au/studio/Tarrowby%20Lisdane%202.jpg

Target Market(s)

30-70yr old (typically wealthy) property buyers, developers and investors

Industry/Entity Type

Vesslane Studio

Number of Pages Required

2 page

Font styles to use
Serif
Sans Serif

Requirements
Must have
• Home page design
• a Content Page design (ie, top nav with sidebar)
Nice to have
• Use any Dorian Vessey Kent images you can find via google etc as placeholders for our own photography (ie they don't need to be licensed as we will be replacing with our own commissioned photography). Full color preferred but feel free to experiment with treating any images as you see fit.

```html
<!DOCTYPE html>
<html lang="en">
<head>
<meta charset="utf-8">
<title>Architecture Practice – Home</title>
<link href="https://fonts.googleapis.com/css2?family=Open+Sans:wght@400;600;700&display=swap" rel="stylesheet">
<style>
:root{
  --blue:#1f7fc4;
  --blue-dark:#14609a;
  --ink:#333;
  --muted:#777;
  --nav:#2d2d2d;
  --line:#dcdcdc;
  --page:#f2f2f2;
  --footer:#2a2a2a;
  --footer-bottom:#1c1c1c;
}
*{box-sizing:border-box;margin:0;padding:0}
html,body{width:679px;height:1200px;overflow:hidden}
body{font-family:"Open Sans",Arial,sans-serif;color:var(--ink);background:var(--page);font-size:6px;line-height:1.5}
.wrap{width:566px;margin:0 auto;background:#fff;height:1200px;position:relative}
a{color:inherit;text-decoration:none}

/* header */
.site-header{height:60px;display:flex;align-items:center;padding:0 6px;position:relative}
.brand{display:flex;align-items:center;gap:6px;font-size:14px;font-weight:600;color:var(--ink)}
.brand i{width:12px;height:12px;background:var(--blue);display:inline-block}
.call{position:absolute;left:333px;top:22px;display:flex;align-items:center;gap:5px;font-size:9px;color:#555}
.search{position:absolute;right:8px;top:21px;display:flex}
.search span{width:58px;height:13px;border:1px solid var(--line);background:#fff}
.search b{width:22px;height:13px;background:var(--blue);color:#fff;font-size:5.5px;font-weight:600;display:flex;align-items:center;justify-content:center}

/* nav */
.main-nav{height:22px;background:var(--blue);display:flex}
.main-nav a{width:72px;height:22px;display:flex;align-items:center;justify-content:center;color:#fff;font-size:7px;font-weight:600;border-right:1px solid rgba(255,255,255,.18)}
.main-nav a.active{background:var(--nav)}

/* hero */
.hero{position:relative;height:258px;margin-top:8px}
.hero-photo{position:absolute;inset:0;background:linear-gradient(160deg,#9fb6cf 0%,#c7d2dc 35%,#7f8fa2 65%,#3e4a5c 100%)}
.hero-caption{position:absolute;left:210px;top:74px;width:335px;background:rgba(255,255,255,.82);padding:9px 12px}
.hero-caption h1{color:var(--blue);font-size:14px;font-weight:700;line-height:1.2}
.hero-caption p{font-size:6px;color:#444;margin-top:4px;text-transform:uppercase;line-height:1.4}

/* welcome */
.welcome{text-align:center;padding:26px 22px 0}
.welcome h2{font-size:16px;font-weight:600;color:#444}
.welcome p{margin-top:10px;color:var(--muted);font-size:6px;line-height:1.7;text-align:center}
.welcome p a{color:var(--blue)}

/* projects */
.projects{margin-top:26px;height:296px;background:linear-gradient(180deg,#f4f4f4,#e6e6e6);border-top:1px solid var(--line);border-bottom:1px solid var(--line);padding-top:22px}
.projects h2{font-size:15px;font-weight:600;color:#444;text-align:center}
.projects h2::after{content:"";display:block;width:70px;height:1px;background:#bbb;margin:6px auto 0}
.cards{display:flex;gap:6px;margin:14px 10px 0}
.card{flex:1;background:#fff;box-shadow:0 1px 3px rgba(0,0,0,.15)}
.card-photo{height:108px}
.card-photo.a{background:linear-gradient(135deg,#d9dbe0,#9aa3ad)}
.card-photo.b{background:linear-gradient(135deg,#3c4a3a,#7e8c78)}
.card-photo.c{background:linear-gradient(135deg,#8aa7c8,#b59f74)}
.card-body{padding:8px 8px 10px}
.card h4{font-size:7px;font-weight:700;color:#333}
.card p{color:var(--muted);margin-top:3px}
.btn{display:inline-block;margin-top:6px;background:var(--blue-dark);color:#fff;font-size:5.5px;padding:2px 7px}

/* lower */
.lower{display:flex;gap:16px;padding:30px 12px 0;height:250px}
.col{flex:1}
.col h3{font-size:9px;font-weight:600;text-align:left;display:flex;align-items:center;gap:5px;color:#444}
.col h3 i{width:9px;height:9px;border-radius:50%;border:2px solid var(--blue);display:inline-block}
.featured{border:1px solid var(--line);box-shadow:0 1px 3px rgba(0,0,0,.12)}
.featured h3{background:var(--blue);color:#fff;padding:7px 8px}
.featured h3 i{border-color:#fff}
.featured ul{list-style:none;padding:4px 10px 8px}
.featured li{padding:5px 0 5px 10px;border-bottom:1px solid #eee;color:#555;position:relative}
.featured li::before{content:"";position:absolute;left:0;top:8px;width:4px;height:4px;border-radius:50%;background:var(--blue)}
.post{display:flex;gap:7px;margin-top:12px}
.post-photo{width:60px;height:40px;flex:none;background:linear-gradient(135deg,#7e97b3,#c4cfdb)}
.post h4{color:var(--blue);font-size:6.5px;font-weight:600}
.post p{color:var(--muted)}
.post a{color:var(--blue)}
.quote{margin-top:12px;border:1px solid var(--line);padding:8px;color:#666;position:relative;line-height:1.6}
.quote::after{content:"";position:absolute;left:14px;bottom:-6px;width:10px;height:10px;background:#fff;border-right:1px solid var(--line);border-bottom:1px solid var(--line);transform:rotate(45deg)}
.author{display:flex;align-items:center;gap:7px;margin-top:14px}
.avatar{width:28px;height:28px;border-radius:50%;background:linear-gradient(135deg,#b8a28c,#6f5e50)}
.author b{color:var(--blue);font-size:7px}
.author span{color:#777}

/* footer */
.site-footer{position:absolute;left:0;right:0;top:1040px;height:134px;background:var(--footer);display:flex;padding:18px 12px 0;gap:14px;color:#bbb}
.site-footer .fcol{flex:1}
.site-footer h5{color:#fff;font-size:7.5px;font-weight:600;padding-bottom:4px;border-bottom:1px solid #444;margin-bottom:6px}
.site-footer ul{list-style:none}
.site-footer li{padding:1px 0}
.fpost{display:flex;gap:5px;margin-bottom:6px}
.fpost div{width:28px;height:18px;background:linear-gradient(135deg,#6c83a0,#aab8c6);flex:none}
.fcontact{display:flex;gap:5px;align-items:flex-start;margin-bottom:4px}
.fcontact i{width:6px;height:6px;background:var(--blue);flex:none;margin-top:2px}
.bottom-bar{position:absolute;left:0;right:0;top:1174px;height:26px;background:var(--footer-bottom);display:flex;align-items:center;justify-content:space-between;padding:0 12px;color:#999}
.social{display:flex;gap:3px}
.social span{width:12px;height:12px;background:var(--blue)}
</style>
</head>
<body>
<div class="wrap">
  <header class="site-header">
    <a class="brand" href="#"><i></i>Vesslane Studio</a>
    <div class="call">
      <svg width="10" height="10" viewBox="0 0 24 24"><path fill="#555" d="M6.6 10.8a15 15 0 006.6 6.6l2.2-2.2c.3-.3.7-.4 1-.2 1.1.4 2.3.6 3.6.6.6 0 1 .4 1 1V20c0 .6-.4 1-1 1A17 17 0 013 4c0-.6.4-1 1-1h3.5c.6 0 1 .4 1 1 0 1.3.2 2.5.6 3.6.1.3 0 .7-.2 1z"/></svg>
      1800 300 61927
    </div>
    <div class="search"><span></span><b>Search</b></div>
  </header>

  <nav class="main-nav">
    <a class="active" href="#">Home</a>
    <a href="#">About</a>
    <a href="#">Service</a>
    <a href="#">Inspiration</a>
    <a href="#">News</a>
    <a href="#">Testimonials</a>
    <a href="#">Contact</a>
  </nav>

  <section class="hero">
    <div class="hero-photo" role="img" aria-label="Curved metallic museum facade under a blue sky"></div>
    <div class="hero-caption">
      <h1>LOREM IPSUM DOLOR SIT AMET</h1>
      <p>Mauris tristique dolor eu scelerisque auctor. Lorem lacinia dignissim erat quis pharetra enim.</p>
    </div>
  </section>

  <section class="welcome">
    <h2>Welcome To Architecture Practice</h2>
    <p>Lorem ipsum dolor sit amet, consectetur adipiscing elit. Cras nec quam mi. Phasellus hendrerit sed lacinia interdum, ornare nulla eu. Donec luctus tincidunt nisi, quis vehicula ut mattis at. Morbi posuere luctus porta. Aliquam vel vulputate rhoncus diam, sit amet tempus nunc. Maecenas quis facilisis ipsum, ut pulvinar lorem. Nam volutpat vel lectus nec pulvinar. Nulla dignissim sed tincidunt. Donec accumsan tristique placerat. Etiam et tempor rutrum dictum, non lacinia ante. Vestibulum placerat, neque eget dignissim pretium, lectus augue. <a href="#">read more</a></p>
  </section>

  <section class="projects">
    <h2>Our Project</h2>
    <div class="cards">
      <article class="card">
        <div class="card-photo a" role="img" aria-label="Interior render of a modern residence"></div>
        <div class="card-body"><h4>LOREM IPSUM DOLOR SIT AMET</h4><p>Lorem ipsum dolor sit amet consectetur adipiscing elit. Praesent odio.</p><a class="btn" href="#">Read More</a></div>
      </article>
      <article class="card">
        <div class="card-photo b" role="img" aria-label="Aerial view of a commercial building site"></div>
        <div class="card-body"><h4>LOREM IPSUM DOLOR SIT AMET</h4><p>Lorem ipsum dolor sit amet consectetur adipiscing elit. Praesent odio.</p><a class="btn" href="#">Read More</a></div>
      </article>
      <article class="card">
        <div class="card-photo c" role="img" aria-label="Riverside museum building with curved roofs"></div>
        <div class="card-body"><h4>LOREM IPSUM DOLOR SIT AMET</h4><p>Lorem ipsum dolor sit amet consectetur adipiscing elit. Praesent odio.</p><a class="btn" href="#">Read More</a></div>
      </article>
    </div>
  </section>

  <section class="lower">
    <div class="col featured">
      <h3><i></i>Featured Work Section</h3>
      <ul>
        <li>Lorem ipsum dolor</li>
        <li>consectetur adipiscing elit</li>
        <li>quam mi Phasellus</li>
        <li>ante pulvinar</li>
        <li>Donec consectetur</li>
        <li>Vestibulum nec augue</li>
      </ul>
    </div>
    <div class="col">
      <h3><i></i>Our Blog</h3>
      <div class="post">
        <div class="post-photo" role="img" aria-label="Museum exterior at dusk"></div>
        <div><h4>Lorem ipsum dolor</h4><p>2 Jan 2013 · 2 comments</p><p>Sit amet, consectetur adipiscing elit. <a href="#">read more</a></p></div>
      </div>
      <div class="post">
        <div class="post-photo" role="img" aria-label="Modern house facade"></div>
        <div><h4>Lorem ipsum dolor</h4><p>5 Jan 2013 · 4 comments</p><p>Sit amet, consectetur adipiscing elit. <a href="#">read more</a></p></div>
      </div>
    </div>
    <div class="col">
      <h3><i></i>Our Testimonials</h3>
      <div class="quote">Lorem ipsum dolor sit amet, consectetur adipiscing elit. Phasellus nec dui dictum, vehicula diam in, pretium lorem. Integer sed luctus nisl, sit amet tempor lacus.</div>
      <div class="author">
        <div class="avatar" role="img" aria-label="Client portrait"></div>
        <div><b>Marla Everton</b> <span>/ Architecture</span></div>
      </div>
    </div>
  </section>

  <footer class="site-footer">
    <div class="fcol">
      <h5>About Us</h5>
      <p>Lorem ipsum dolor sit amet consectetur adipiscing elit. Nullam quis mi lectus. Sed dignissim felis a pulvinar eros blandit in. Cras varius dui.</p>
    </div>
    <div class="fcol">
      <h5>Quick Links</h5>
      <ul><li>Home</li><li>About</li><li>Service</li><li>Inspiration</li><li>News</li><li>Testimonials</li><li>Contact</li></ul>
    </div>
    <div class="fcol">
      <h5>Latest Post</h5>
      <div class="fpost"><div role="img" aria-label="Post thumbnail"></div><p>Lorem ipsum dolor sit amet elit.</p></div>
      <div class="fpost"><div role="img" aria-label="Post thumbnail"></div><p>Lorem ipsum dolor sit amet elit.</p></div>
    </div>
    <div class="fcol">
      <h5>Contact Us</h5>
      <div class="fcontact"><i></i><p>42 Harrow Lane, Suite 9<br>Brindlemoor, NT 2031</p></div>
      <div class="fcontact"><i></i><p>1800 300 61927</p></div>
      <div class="fcontact"><i></i><p>hello@vesslane.net</p></div>
    </div>
  </footer>
  <div class="bottom-bar">
    <span>Copyright © 2013 brand name here</span>
    <div class="social"><span></span><span></span><span></span></div>
  </div>
</div>
</body>
</html>
```